Business card design needed

Our company background is that we provides transfers to and from the airport, social & corporate events, weddings.
We are also available for charter for birthday party, wine tastings, concerts, anniversary, school balls etc.
Our business cards have to reflect that we have a professional company, they are our first contact and have to stand out from the other 'players' in the market.

Industry/Entity Type

School

Contact Information for Business Card

BRISTEL QDF, Laurent & Marisol, mob: 0427 381 594, PO Box 287, Tarrowin WA 6311, ABN 52 914 603 278, Lic 7169/5804,

Requirements
Must have
• Telephone number: 0427 381 594
Website: www.BRISTELQDF.com.au
postal address: PO Box 287, Tarrowin WA 6311
Licences: Lic 7169/5804

***If using the new photo (one with the bus and buildings behind it), if possible can the buildings be cropped out. Thanks
Nice to have
• would be nice to have the pics of the vehicle(s), preferred the Pel on the card but not too fussed.
Should not have
• Picture of vehicle we don't have in our fleet. (We ONLY have the Pellics and Rendak Ovaro mini bus)

```html
<!DOCTYPE html>
<html lang="en">
<head>
<meta charset="utf-8">
<title>BRISTEL QDF – Business Card</title>
<link rel="stylesheet" href="https://fonts.googleapis.com/css2?family=Righteous&family=Questrial&display=swap">
<style>
  :root {
    --page-bg: #e9eaec;
    --card-blue-light: #3f9ad3;
    --card-blue: #1f6fab;
    --card-blue-dark: #0f4c82;
    --panel-top: #f7f8f9;
    --panel-bottom: #c8ccd2;
    --ink-navy: #1c4d7c;
    --title-white: #ffffff;
    --frame-blue: #3aa3e0;
    --photo-sky: #8fa6b4;
    --photo-silver: #a9adb1;
    --photo-road: #6a5446;
  }
  * { box-sizing: border-box; margin: 0; padding: 0; }
  html, body {
    width: 1200px; height: 900px; overflow: hidden;
    background: var(--page-bg);
  }
  .canvas {
    position: relative; width: 1200px; height: 900px;
    display: flex; flex-direction: column; align-items: center; justify-content: center; gap: 30px;
  }
  .card {
    position: relative; width: 720px; height: 412px; border-radius: 22px; overflow: hidden;
    background: radial-gradient(ellipse at 35% 30%, var(--card-blue-light) 0%, var(--card-blue) 55%, var(--card-blue-dark) 100%);
    box-shadow: 0 6px 18px rgba(0,0,0,0.18);
  }
  .brand-name {
    position: absolute; font-family: "Righteous", sans-serif; color: var(--title-white);
    letter-spacing: 2px; white-space: nowrap;
  }
  .info-panel {
    position: absolute; border-radius: 24px;
    background: linear-gradient(180deg, var(--panel-top) 0%, var(--panel-bottom) 100%);
    color: var(--ink-navy); font-family: "Questrial", sans-serif; text-align: center;
  }

  /* Services side */
  .card--services .brand-name { top: 24px; left: 0; right: 0; text-align: center; font-size: 44px; }
  .card--services .info-panel {
    top: 88px; left: 30px; width: 660px; height: 172px; padding: 22px 30px;
    font-size: 21px; line-height: 1.35;
  }
  .service-line + .service-line { margin-top: 12px; }
  .service-label { font-weight: bold; font-size: 25px; }
  .fleet-strip {
    position: absolute; left: 12px; bottom: 16px; display: flex; gap: 8px;
  }
  .fleet-photo {
    width: 168px; height: 124px; border: 6px solid var(--frame-blue);
    background: linear-gradient(180deg, var(--photo-sky) 0%, var(--photo-silver) 55%, var(--photo-road) 100%);
  }
  .fleet-photo--bus {
    background: linear-gradient(180deg, var(--photo-sky) 0%, #e4e6e8 50%, var(--photo-road) 100%);
  }

  /* Contact side */
  .card--contact .brand-name { top: 40px; left: 0; right: 0; text-align: center; font-size: 54px; }
  .card--contact .info-panel {
    top: 120px; left: 90px; width: 600px; height: 262px; padding: 30px 30px;
    font-size: 22px; line-height: 1.3;
  }
  .contact-names { font-weight: bold; font-size: 25px; margin-bottom: 12px; }
  .contact-row { display: flex; justify-content: center; align-items: flex-start; gap: 14px; margin-bottom: 12px; }
  .contact-icon { width: 18px; height: 18px; margin-top: 4px; flex: none; fill: var(--ink-navy); }
  .licence { margin-top: 8px; }
</style>
</head>
<body>
<main class="canvas">
  <section class="card card--services">
    <h1 class="brand-name">BRISTEL QDF</h1>
    <div class="info-panel">
      <p class="service-line"><span class="service-label">Transfers:</span> to and from the airport, social &amp; corporate events, weddings</p>
      <p class="service-line"><span class="service-label">Charter for:</span> birthday party, wine tastings, concerts, anniversary, school balls</p>
    </div>
    <div class="fleet-strip">
      <div class="fleet-photo" role="img" aria-label="Photo of a silver Pel sedan"></div>
      <div class="fleet-photo" role="img" aria-label="Photo of the front of a silver Pel sedan"></div>
      <div class="fleet-photo" role="img" aria-label="Photo of a silver Pel sedan from the side"></div>
      <div class="fleet-photo fleet-photo--bus" role="img" aria-label="Photo of the white Rendak Ovaro mini bus"></div>
    </div>
  </section>

  <section class="card card--contact">
    <h2 class="brand-name">BRISTEL QDF</h2>
    <div class="info-panel">
      <p class="contact-names">Laurent &amp; Marisol</p>
      <p class="contact-row">
        <svg class="contact-icon" viewBox="0 0 18 18" aria-hidden="true"><path d="M5 1h8a1.5 1.5 0 0 1 1.5 1.5v13A1.5 1.5 0 0 1 13 17H5a1.5 1.5 0 0 1-1.5-1.5v-13A1.5 1.5 0 0 1 5 1zm.5 2v10.5h7V3z"/></svg>
        <span>0427 381 594</span>
      </p>
      <p class="contact-row">
        <svg class="contact-icon" viewBox="0 0 18 18" aria-hidden="true"><path d="M9 1.5 1 8.5h2.2V16h4.3v-4.5h3V16h4.3V8.5H17z"/></svg>
        <span>PO Box 287, Tarrowin WA 6311,<br>ABN 52 914 603 278</span>
      </p>
      <p class="licence">Lic 7169/5804</p>
    </div>
  </section>
</main>
</body>
</html>
```